Flyer-Design für Gefäßchirurg
Zielgruppe
Niedergelassener Gefäßchirurg in eigener (Einzel-) Praxis; zZt 4 Angestellte (1 Krankenschwester, eine MFA, eine Azubi, eine Reinigungskraft); tätig in der Stadt Plön (24306); im Kreis Plön nur ein weiter ALLGEMEIN chirurg; HP: www.praxisdoktor-haverbeck.de ; Kernkompetenz: Diagnostik und Therapie von Gefäßerkrankungen (z.B. Krampfadern, Durchblutungsstörungen... (s.auch HP); eigener OP in der Praxis; hier Versorgung u.a. von Krampfadern aber auch andere chirurgische Eingriffe;
Aufgabenstellung
Bzgl. des Formates keine Festlegung bevorzuge aber Format Din lang hoch oder Din a 5 hoch ; Flyer soll übersichtlich Behandlungen der Praxis benennen; insbesondere um auch außerhalb der Gefäßchirurgie weitere chirurgische Patienten zu gewinnen (z.B. chirurgische Entfernung kleiner Pigmentflecke, eingewachsener Nagel, aber auch 'Wegspritzen/ Sklerosierung' von Besenreisern, eingewachsener Zehennagel), ggf. mit Anfahrtskarte, Parkplätze vor der Tür; falls nicht zu Kostenintensiv: auch Nutzung von Stock - Bildern (ca. Obergrenze für Bildmaterial 50,- €);
mir ist bewusst, dass die Photos der Angestellten und mir nicht 100% scharf sind; falls diese verwendet werden, könnten diese z.B. kleinformatig auf dem flyer erscheinen, oder ich würde diese im Verlauf noch einmal aufnehmen. Ob und wieviele der Photos auf dem flyer sind, überlasse ich Ihnen.

```html
<!DOCTYPE html>
<html lang="de">
<head>
<meta charset="utf-8">
<title>Flyer Gefäßmedizin Plön</title>
<link rel="stylesheet" href="https://fonts.googleapis.com/css2?family=Ubuntu:wght@300;500;700&family=Arimo:wght@400;700&display=swap">
<style>
  :root {
    --red: #c8133a;
    --red-dark: #9c0b2c;
    --blue: #3e56a5;
    --blue-dark: #2d438f;
    --white: #ffffff;
    --stage: #d9d9d9;
    --head: "Ubuntu", sans-serif;
    --body: "Arimo", sans-serif;
  }
  * { box-sizing: border-box; margin: 0; padding: 0; }
  html, body { width: 1200px; height: 765px; overflow: hidden; }
  body {
    background: var(--stage);
    font-family: var(--body);
    color: var(--white);
    position: relative;
  }
  .spread {
    position: absolute;
    top: 72px;
    width: 560px;
    height: 620px;
    display: flex;
    box-shadow: 0 6px 18px rgba(0,0,0,.25);
  }
  .spread--inner { left: 20px; }
  .spread--outer { left: 620px; }
  .panel {
    position: relative;
    width: 280px;
    height: 620px;
    overflow: hidden;
  }
  .band { position: absolute; left: 0; width: 100%; }
  .band--blue { background: linear-gradient(160deg, var(--blue-dark), var(--blue) 60%, #4a62b0); }
  .band--red { background: linear-gradient(160deg, var(--red-dark), var(--red) 55%, #d4173f); }
  .band--texture {
    background: radial-gradient(circle at 40% 40%, #d8224a, var(--red) 45%, var(--red-dark));
  }
  .heading {
    font-family: var(--head);
    font-weight: 700;
    font-size: 17px;
    position: absolute;
    left: 26px;
  }
  .copy {
    position: absolute;
    left: 26px;
    right: 22px;
    font-size: 8.2px;
    line-height: 1.35;
  }
  .copy p { margin-bottom: 9px; }
  .bullets { list-style: none; }
  .bullets li {
    position: relative;
    padding-left: 12px;
    margin-bottom: 3px;
  }
  .bullets li::before {
    content: "";
    position: absolute;
    left: 0; top: 5px;
    width: 3px; height: 3px;
    background: var(--white);
    border-radius: 50%;
  }
  .services { font-size: 9px; line-height: 1.35; }
  .services li { margin-bottom: 5px; }
  .photo {
    position: absolute;
    background: linear-gradient(170deg, #d9d4cc, #8f8a86);
    border: 3px solid var(--white);
  }
  .photo--doctor { left: 30px; top: 280px; width: 92px; height: 122px; }
  .team-photo { top: 400px; width: 74px; height: 90px; }
  .team-name {
    position: absolute;
    top: 498px;
    width: 74px;
    font-family: var(--head);
    font-weight: 500;
    font-size: 9px;
    text-align: center;
  }
  .doctor-name {
    position: absolute;
    left: 26px; top: 418px;
    font-family: var(--head);
    font-weight: 700;
    font-size: 13px;
  }
  .practice-name {
    position: absolute;
    right: 22px; top: 348px;
    font-family: var(--head);
    font-weight: 500;
    font-size: 11px;
    display: flex;
    align-items: center;
    gap: 6px;
  }
  .practice-name .dot {
    width: 8px; height: 8px;
    border-radius: 50%;
    background: var(--white);
  }
  .greeting {
    position: absolute;
    left: 0; right: 0; bottom: 36px;
    text-align: center;
    font-family: var(--head);
    font-weight: 500;
    font-size: 15px;
  }
  .hours {
    position: absolute;
    left: 26px; top: 228px;
    font-size: 8px;
    border-collapse: collapse;
  }
  .hours td { padding: 1px 12px 1px 0; }
  .contact { top: 352px; font-size: 7.8px; }
  .contact p { margin-bottom: 7px; }
  .map {
    position: absolute;
    left: 26px; top: 470px;
    width: 150px; height: 104px;
    background: linear-gradient(135deg, #f1f1f1, #e2e2e2 60%, #b8d5ea);
    border: 2px solid var(--white);
  }
  .cover-name {
    position: absolute;
    left: 20px; top: 42px;
    font-family: var(--head);
    font-weight: 300;
    font-size: 21px;
  }
  .cover-title {
    position: absolute;
    left: 18px; top: 82px;
    font-family: var(--head);
    font-weight: 700;
    font-size: 26px;
    line-height: 1.12;
  }
  .cover-address {
    position: absolute;
    left: 20px; top: 470px;
    font-family: var(--head);
    font-weight: 700;
    font-size: 12px;
    line-height: 1.3;
  }
  .cover-web {
    position: absolute;
    left: 20px; top: 548px;
    font-family: var(--head);
    font-weight: 700;
    font-size: 10px;
  }
</style>
</head>
<body>

<section class="spread spread--inner">
  <article class="panel panel--welcome">
    <div class="band band--blue" style="top:0;height:340px"></div>
    <div class="band band--texture" style="top:340px;height:280px" role="img" aria-label="Rote Nahaufnahme von Blutkörperchen als Hintergrund"></div>
    <h2 class="heading" style="top:34px">Herzlich Willkommen</h2>
    <div class="copy" style="top:64px">
      <p>Gerne kümmern wir uns um Ihre gefäßmedizinischen und chirurgischen Anliegen.</p>
      <p>Als Gefäßchirurg und Phlebologe besitze ich eine besondere Erfahrung in der Therapie und Diagnostik von gefäßmedizinischen Erkrankungen.</p>
      <p>Mit einem hochwertigen Ultraschallgerät sowie durch einen in die Praxis integrierten Operationsraum und einem Aufwachraum sind optimale Bedingungen gegeben.</p>
      <p>Bezüglich der operativen Versorgung des Krampfaderleidens halten wir alle gängigen Operationsmethoden vor.</p>
      <p>Abseits der gefäßmedizinischen Erkrankungen sind wir auch für kleinere chirurgischen Maßnahmen Ihr Ansprechpartner.</p>
    </div>
    <div class="photo photo--doctor" role="img" aria-label="Porträtfoto des Praxisinhabers"></div>
    <h3 class="doctor-name">Dr. Jonas Haverbeck</h3>
    <ul class="copy bullets" style="top:442px">
      <li>Ehemals leitender Oberarzt in der Klinik für Gefäßmedizin in Schleswig</li>
      <li>Endovaskulärer Chirurg</li>
      <li>Weiterbildung zum Phlebologen („Venenspezialist“)</li>
      <li>Prüfung in der Ultraschalldiagnostik</li>
      <li>Doppler/ Duplexsonographie extrakranieller Gefäße (Gefäße des Halses)</li>
      <li>Ultraschalldiagnostik Doppler/ Duplexsonographie der peripheren Venen und Arterien</li>
    </ul>
  </article>

  <article class="panel panel--services">
    <div class="band band--red" style="top:0;height:440px"></div>
    <div class="band band--blue" style="top:440px;height:180px"></div>
    <h2 class="heading" style="top:30px">Leistungen</h2>
    <ul class="copy bullets services" style="top:62px">
      <li>Krampfadern</li>
      <li>Besenreiser</li>
      <li>Schaufensterkrankheit - Durchblutungsstörung der Beine</li>
      <li>Bauchaortenaneurysma - Erweiterungen der Bauch- und Beckenschlagader</li>
      <li>Bewertung des Schlaganfallsrisikos</li>
      <li>Durchblutungsstörung der Hände und Füße</li>
      <li>Pigmentflecken oder kleine Hauttumore</li>
      <li>Nagelbettentzündung</li>
      <li>Steißbeinfistel</li>
    </ul>
    <div class="practice-name"><span class="dot"></span>Dr. Jonas Haverbeck</div>
    <h2 class="heading" style="top:376px">Das Team</h2>
    <div class="photo team-photo" style="left:22px" role="img" aria-label="Porträtfoto Mitarbeiterin Selin"></div>
    <div class="photo team-photo" style="left:103px" role="img" aria-label="Porträtfoto Mitarbeiterin Katrin"></div>
    <div class="photo team-photo" style="left:184px" role="img" aria-label="Porträtfoto Mitarbeiterin Lena"></div>
    <span class="team-name" style="left:22px">Selin</span>
    <span class="team-name" style="left:103px">Katrin</span>
    <span class="team-name" style="left:184px">Lena</span>
    <p class="greeting">Wir freuen uns auf Sie.</p>
  </article>
</section>

<section class="spread spread--outer">
  <article class="panel panel--info">
    <div class="band band--red" style="top:0;height:300px"></div>
    <div class="band band--blue" style="top:300px;height:320px"></div>
    <h2 class="heading" style="top:30px">Terminvergabe</h2>
    <div class="copy" style="top:56px;font-size:7.6px">
      <p>Wir bieten unseren Patienten eine Terminsprechstunde an. Dies hat den Vorteil, dass Wartezeiten auf ein Minimum beschränkt werden.</p>
      <p>Gerne vergeben wir Ihnen unter Telefon 04522 555 0140 einen für Sie passenden Termin.</p>
      <p>Für ein akutes Problem wenden Sie sich bitte an die entsprechenden Einrichtungen, alternativ bieten wir auch zu bestimmten Zeiten eine offene Sprechstunde an. Diese Zeiten entnehmen Sie der Internetpräsenz des Ärztlichen Notdienstes der Region.</p>
    </div>
    <h2 class="heading" style="top:204px">Öffnungszeiten</h2>
    <table class="hours">
      <tr><td>Montag:</td><td>8:00 - 13:00</td><td></td></tr>
      <tr><td>Dienstag:</td><td>8:00 - 13:00</td><td>15:00 - 18:00</td></tr>
      <tr><td>Mittwoch:</td><td>8:00 - 13:00</td><td></td></tr>
      <tr><td>Donnerstag:</td><td>8:00 - 13:00</td><td></td></tr>
      <tr><td>Freitag:</td><td>8:00 - 13:00</td><td></td></tr>
    </table>
    <h2 class="heading" style="top:322px">Anfahrt &amp; Kontakt</h2>
    <div class="copy contact">
      <p>Dr. Jonas Haverbeck<br>Praxis für Gefäßmedizin, Gefäßchirurgie<br>und Phlebologie</p>
      <p>Lindenweg 12<br>24306 Plön</p>
      <p>04522 555 0140<br>04522 555 0149<br>info@praxisdoktor-haverbeck.de</p>
    </div>
    <div class="map" role="img" aria-label="Anfahrtskarte zur Praxis mit Parkplätzen vor der Tür"></div>
  </article>

  <article class="panel panel--cover">
    <div class="band band--blue" style="top:0;height:300px"></div>
    <div class="band band--texture" style="top:300px;height:320px" role="img" aria-label="Rote Nahaufnahme von Blutkörperchen als Hintergrund"></div>
    <p class="cover-name">Dr. Jonas Haverbeck</p>
    <h1 class="cover-title">Gefäßmedizin<br>Gefäßchirurgie<br>Phlebologie</h1>
    <p class="cover-address">Lindenweg 12<br>24306 Plön</p>
    <p class="cover-web">www.praxisdoktor-haverbeck.de</p>
  </article>
</section>

</body>
</html>
```